Re-Design the flow of the Keystride Principles

The keystride principle is a 10 step model that helps teams/organizations become high performing. Attached the model which i created. I love the design as it is but i used a template i don't owe the rights of so i would like to use this platform to see what you can come up with the redesign this flow while keeping the key elements in place. I like the flow, i like the cleanness and i like it to be compact.

Target Market(s)

Organizational change / Leadership/ Consultancy

Industry/Entity Type

Leadership

Requirements
Must have
• Keep as much as possible the flow and feel of the attached
Nice to have
• -Maybe some twist in how the different parts connect (not a must)
Should not have
• Less or more steps than added in the attached file

```html
<!DOCTYPE html>
<html lang="en">
<head>
<meta charset="utf-8">
<title>The Keystride Principles</title>
<link rel="stylesheet" href="https://fonts.googleapis.com/css2?family=Roboto+Condensed:wght@700;800&family=Source+Sans+3:wght@400;600;700&display=swap">
<style>
  :root {
    --bg: #000000;
    --paper: #ffffff;
    --paper-edge: #e4e4ea;
    --paper-shade: #cfcfd6;
    --ink-grey: #4f4f55;
    --title-blue: #4a9ad6;
    --blue-dark: #0f5a9c;
    --blue-text: #1b6fb5;
    --indigo: #3f55a8;
    --violet: #5b3a8f;
    --sky: #1b8ac8;
    --sky-text: #2398d2;
    --teal: #2fb0bf;
    --lime: #86b81f;
    --purple: #8e2d8e;
    --pink: #d9336b;
    --orange: #e8631f;
    --gold: #d9a800;
  }
  html, body {
    margin: 0;
    padding: 0;
    background: var(--bg);
    overflow: hidden;
  }
  .canvas {
    position: relative;
    width: 1200px;
    height: 880px;
    background: var(--bg);
    overflow: hidden;
    font-family: "Source Sans 3", sans-serif;
  }
  .headline {
    position: absolute;
    left: 0;
    right: 0;
    top: 40px;
    margin: 0;
    text-align: center;
    font-family: "Roboto Condensed", sans-serif;
    font-weight: 800;
    font-size: 60px;
    line-height: 1;
    color: var(--paper);
    letter-spacing: -0.5px;
  }
  .headline .accent { color: var(--title-blue); }
  .tagline {
    position: absolute;
    left: 0;
    right: 0;
    top: 114px;
    margin: 0;
    text-align: center;
    font-family: "Roboto Condensed", sans-serif;
    font-weight: 700;
    font-size: 17px;
    color: var(--paper);
    letter-spacing: 0.2px;
  }
  .model { position: absolute; left: 0; top: 0; }
  .step-label {
    font-family: "Source Sans 3", sans-serif;
    font-size: 13.5px;
    font-weight: 600;
  }
  .arc-label {
    font-family: "Roboto Condensed", sans-serif;
    font-weight: 700;
    font-size: 20px;
    letter-spacing: 5px;
    fill: var(--paper);
  }
  .hub-label { font-size: 14px; fill: var(--paper); }
  .outcome { font-size: 13px; fill: var(--ink-grey); font-weight: 600; }
  .metric { font-size: 10.5px; fill: var(--ink-grey); }
  .start-label { font-size: 13px; font-weight: 700; fill: var(--ink-grey); }
</style>
</head>
<body>
<div class="canvas">
  <h1 class="headline">THE <span class="accent">KEYSTRIDE</span> PRINCIPLES</h1>
  <p class="tagline">LIBERATE THE WORKPLACE UNLEASHING VALUE THROUGH PURPOSE AT EVERY LEVEL OF SCALE</p>

  <svg class="model" width="1200" height="880" viewBox="0 0 1200 880" aria-label="Ten step Keystride model in two linked wheels">
    <defs>
      <radialGradient id="wheelLeft" cx="300" cy="520" r="240" gradientUnits="userSpaceOnUse">
        <stop offset="0.4" stop-color="var(--paper-shade)"/>
        <stop offset="0.7" stop-color="var(--paper)"/>
        <stop offset="1" stop-color="var(--paper-edge)"/>
      </radialGradient>
      <radialGradient id="wheelRight" cx="900" cy="520" r="240" gradientUnits="userSpaceOnUse">
        <stop offset="0.4" stop-color="var(--paper-shade)"/>
        <stop offset="0.7" stop-color="var(--paper)"/>
        <stop offset="1" stop-color="var(--paper-edge)"/>
      </radialGradient>
      <linearGradient id="linkShade" x1="0" y1="0" x2="1" y2="0">
        <stop offset="0" stop-color="var(--paper-shade)"/>
        <stop offset="1" stop-color="var(--paper)"/>
      </linearGradient>
      <linearGradient id="startShade" x1="0" y1="0" x2="0" y2="1">
        <stop offset="0" stop-color="var(--paper)"/>
        <stop offset="1" stop-color="var(--paper-shade)"/>
      </linearGradient>
      <path id="arcSelf" d="M81.8,646 A252,252 0 0 1 93.6,375.4"/>
      <path id="arcHuman" d="M121.8,341.8 A252,252 0 0 1 528.4,413.5"/>
      <path id="arcEngage" d="M641.6,614.1 A275,275 0 0 0 1158.4,614.1"/>
    </defs>

    <!-- wheels -->
    <circle cx="300" cy="520" r="240" fill="url(#wheelLeft)"/>
    <circle cx="900" cy="520" r="240" fill="url(#wheelRight)"/>

    <!-- link between wheels -->
    <path class="wheel-link" d="M552,496 L628,496 L650,520 L628,544 L552,544 L574,520 Z" fill="url(#linkShade)"/>

    <!-- left ring: six foundation steps -->
    <g class="ring-left" fill="none" stroke-width="44">
      <circle cx="300" cy="520" r="108" stroke="var(--lime)" stroke-dasharray="113.1 565.5" transform="rotate(60 300 520)"/>
      <circle cx="300" cy="520" r="108" stroke="var(--teal)" stroke-dasharray="113.1 565.5" transform="rotate(120 300 520)"/>
      <circle cx="300" cy="520" r="108" stroke="var(--sky)" stroke-dasharray="113.1 565.5" transform="rotate(180 300 520)"/>
      <circle cx="300" cy="520" r="108" stroke="var(--blue-dark)" stroke-dasharray="113.1 565.5" transform="rotate(240 300 520)"/>
      <circle cx="300" cy="520" r="108" stroke="var(--indigo)" stroke-dasharray="113.1 565.5" transform="rotate(300 300 520)"/>
      <circle cx="300" cy="520" r="108" stroke="var(--violet)" stroke-dasharray="113.1 565.5"/>
    </g>

    <!-- right ring: four excellence steps -->
    <g class="ring-right" fill="none" stroke-width="44">
      <circle cx="900" cy="520" r="108" stroke="var(--gold)" stroke-dasharray="84.82 593.76"/>
      <circle cx="900" cy="520" r="108" stroke="var(--orange)" stroke-dasharray="84.82 593.76" transform="rotate(45 900 520)"/>
      <circle cx="900" cy="520" r="108" stroke="var(--pink)" stroke-dasharray="84.82 593.76" transform="rotate(90 900 520)"/>
      <circle cx="900" cy="520" r="108" stroke="var(--purple)" stroke-dasharray="84.82 593.76" transform="rotate(135 900 520)"/>
    </g>

    <!-- dividers -->
    <g class="dividers" stroke="var(--bg)" stroke-width="8">
      <line x1="56" y1="520" x2="544" y2="520"/>
      <line x1="178" y1="308.7" x2="422" y2="731.3"/>
      <line x1="422" y1="308.7" x2="178" y2="731.3"/>
      <line x1="656" y1="520" x2="1144" y2="520"/>
      <line x1="900" y1="520" x2="1072" y2="692"/>
      <line x1="900" y1="520" x2="900" y2="764"/>
      <line x1="900" y1="520" x2="728" y2="692"/>
    </g>

    <!-- hubs -->
    <circle cx="300" cy="520" r="84" fill="var(--bg)"/>
    <circle cx="900" cy="520" r="84" fill="var(--bg)"/>

    <!-- icons -->
    <g class="icons" fill="var(--paper)" stroke="var(--paper)">
      <g transform="translate(300,412) scale(0.85)" stroke="none">
        <circle cx="-11" cy="-12" r="3.5"/><circle cx="0" cy="-13" r="3.8"/><circle cx="11" cy="-12" r="3.5"/>
        <path d="M-17,-6 h11 l1,10 h-2 v10 h-3 v-10 h-1 v10 h-3 v-10 h-2 Z"/>
        <path d="M-6,-7 h12 l1,11 h-2 v11 h-3 v-11 h-1 v11 h-3 v-11 h-2 Z"/>
        <path d="M6,-6 h11 l1,10 h-2 v10 h-3 v-10 h-1 v10 h-3 v-10 h-2 Z"/>
      </g>
      <g transform="translate(393.5,466) scale(0.85)">
        <path stroke="none" d="M0,15 C-22,0 -20,-16 -10,-16 C-4,-16 0,-11 0,-9 C0,-11 4,-16 10,-16 C20,-16 22,0 0,15Z"/>
        <polyline fill="none" stroke="var(--indigo)" stroke-width="2" points="-12,-2 -6,-2 -3,-8 1,4 4,-4 6,-2 12,-2"/>
      </g>
      <g transform="translate(393.5,574) scale(0.85)" stroke="none">
        <circle cx="-10" cy="-10" r="3"/><circle cx="-2" cy="-11" r="3"/><circle cx="6" cy="-10" r="3"/>
        <rect x="-13" y="-6" width="6" height="10"/><rect x="-5" y="-7" width="6" height="11"/><rect x="3" y="-6" width="6" height="10"/>
        <polyline fill="none" stroke="var(--paper)" stroke-width="2.5" points="-16,12 -6,4 0,8 14,-4"/>
        <path d="M10,-7 L17,-7 L16,0 Z"/>
      </g>
      <g transform="translate(206.5,466) scale(0.85)" fill="none" stroke-width="2.5">
        <circle r="16"/><circle r="9"/><circle r="2.5" fill="var(--paper)"/>
        <line x1="0" y1="-22" x2="0" y2="-12"/><line x1="0" y1="12" x2="0" y2="22"/>
        <line x1="-22" y1="0" x2="-12" y2="0"/><line x1="12" y1="0" x2="22" y2="0"/>
      </g>
      <g transform="translate(206.5,574) scale(0.85)" stroke-width="2.5" fill="none">
        <line x1="-12" y1="-4" x2="14" y2="-14" stroke-width="6"/>
        <line x1="0" y1="-6" x2="-8" y2="16"/><line x1="0" y1="-6" x2="8" y2="16"/><line x1="0" y1="-6" x2="0" y2="16"/>
      </g>
      <g transform="translate(300,628) scale(0.85)">
        <path stroke="none" d="M0,15 C-22,0 -20,-16 -10,-16 C-4,-16 0,-11 0,-9 C0,-11 4,-16 10,-16 C20,-16 22,0 0,15Z"/>
        <polyline fill="none" stroke="var(--lime)" stroke-width="2" points="-12,-2 -6,-2 -3,-8 1,4 4,-4 6,-2 12,-2"/>
      </g>
      <g transform="translate(800,561) scale(0.85)" stroke="none">
        <path d="M-10,16 v-8 c-6,-4 -8,-10 -6,-16 c3,-8 14,-10 20,-4 c4,4 4,8 4,10 l4,6 h-4 v6 h-6 v6 Z"/>
        <circle cx="-4" cy="-6" r="4" fill="var(--purple)"/><circle cx="4" cy="0" r="3" fill="var(--purple)"/>
      </g>
      <g transform="translate(858.7,619.8) scale(0.85)" stroke-width="4" stroke-linecap="round">
        <line x1="0" y1="-16" x2="0" y2="16"/><line x1="-15" y1="-5" x2="15" y2="5"/>
        <line x1="-10" y1="13" x2="10" y2="-13"/><line x1="-10" y1="-13" x2="10" y2="13"/>
        <circle r="4" fill="var(--pink)" stroke="none"/>
      </g>
      <g transform="translate(941.3,619.8) scale(0.85)" stroke="none">
        <path d="M-9,-14 h18 v6 c0,8 -4,12 -9,13 c-5,-1 -9,-5 -9,-13 Z"/>
        <path d="M-9,-11 h-5 c0,6 3,9 6,9" fill="none" stroke="var(--paper)" stroke-width="2.5"/>
        <path d="M9,-11 h5 c0,6 -3,9 -6,9" fill="none" stroke="var(--paper)" stroke-width="2.5"/>
        <rect x="-2" y="4" width="4" height="6"/><rect x="-8" y="10" width="16" height="4"/>
      </g>
      <g transform="translate(1000,561) scale(0.85)" fill="none" stroke-width="3">
        <circle cx="-3" cy="-4" r="11"/>
        <line x1="4" y1="5" x2="10" y2="17" stroke-width="5" stroke-linecap="round"/>
        <polyline stroke-width="1.8" points="-10,-4 -6,-4 -4,-9 -1,1 1,-4 4,-4"/>
      </g>
    </g>

    <!-- step labels -->
    <g class="step-label" text-anchor="middle">
      <text fill="var(--lime)"><tspan x="300" y="694">Discover your</tspan><tspan x="300" dy="16">purpose. Why</tspan><tspan x="300" dy="16">Do you exist?</tspan></text>
      <text fill="var(--teal)"><tspan x="139" y="591">Identify</tspan><tspan x="139" dy="16">Purpose</tspan><tspan x="139" dy="16">Activators</tspan><tspan x="139" dy="16">(Vision)</tspan></text>
      <text fill="var(--sky-text)"><tspan x="139" y="415">Develop a</tspan><tspan x="139" dy="16">Master plan</tspan><tspan x="139" dy="16">(strategy)</tspan></text>
      <text fill="var(--blue-text)"><tspan x="300" y="314">Cultivate</tspan><tspan x="300" dy="16">Psychological</tspan><tspan x="300" dy="16">Safety and</tspan><tspan x="300" dy="16">Ownership</tspan></text>
      <text fill="var(--indigo)"><tspan x="455" y="410">Tap into peoples</tspan><tspan x="455" dy="16">Purpose and</tspan><tspan x="455" dy="16">Passion (intrinsic</tspan><tspan x="455" dy="16">motivation)</tspan></text>
      <text fill="var(--violet)"><tspan x="463" y="606">Unlock culture of</tspan><tspan x="463" dy="16">personal growth</tspan><tspan x="463" dy="16">&amp; development</tspan></text>
      <text fill="var(--purple)"><tspan x="728" y="577">Prioritize</tspan><tspan x="728" dy="16">Feedback &amp;</tspan><tspan x="728" dy="16">Transparency</tspan></text>
      <text fill="var(--pink)"><tspan x="829" y="678">Empower the</tspan><tspan x="829" dy="16">community from</tspan><tspan x="829" dy="16">bottom up</tspan></text>
      <text fill="var(--orange)"><tspan x="975" y="678">Put excellent (team)</tspan><tspan x="975" dy="16">performance in</tspan><tspan x="975" dy="16">the spotlight</tspan></text>
      <text fill="var(--gold)"><tspan x="1072" y="577">Monitor</tspan><tspan x="1072" dy="16">engagement</tspan><tspan x="1072" dy="16">Real-time</tspan></text>
    </g>

    <!-- hub labels -->
    <text class="hub-label" text-anchor="middle"><tspan x="300" y="505">Capabilities</tspan><tspan x="300" dy="17">driving a solid</tspan><tspan x="300" dy="17">foundation</tspan></text>
    <text class="hub-label" text-anchor="middle"><tspan x="900" y="505">Capabilities</tspan><tspan x="900" dy="17">maximizing</tspan><tspan x="900" dy="17">excellence</tspan></text>

    <!-- outcome -->
    <g class="outcome-block">
      <path d="M887,300 h26 l8,9 l-21,22 l-21,-22 Z M879,309 h42 M893,300 l-4,9 l11,22 l11,-22 l-4,-9" fill="none" stroke="var(--ink-grey)" stroke-width="2.5" stroke-linejoin="round"/>
      <text class="outcome" text-anchor="middle"><tspan x="900" y="360">Reaching full potential of</tspan><tspan x="900" dy="16">people and organization</tspan></text>
      <g class="metric">
        <circle cx="761" cy="408.5" r="1.5" fill="var(--ink-grey)"/><text x="768" y="412">Productivity up to 800%</text>
        <circle cx="761" cy="426.5" r="1.5" fill="var(--ink-grey)"/><text x="768" y="430">Employee engagement &gt;90%</text>
        <circle cx="905" cy="408.5" r="1.5" fill="var(--ink-grey)"/><text x="912" y="412">Max discretionary effort gap</text>
        <circle cx="905" cy="426.5" r="1.5" fill="var(--ink-grey)"/><text x="912" y="430">High resilience to change</text>
      </g>
    </g>

    <!-- start tag -->
    <path class="start-tag" d="M240,796 L300,768 L360,796 L360,852 L240,852 Z" fill="url(#startShade)"/>
    <text class="start-label" text-anchor="middle"><tspan x="300" y="818">START HERE</tspan><tspan x="300" dy="18">INVENT HERE</tspan></text>

    <!-- flow arcs -->
    <text class="arc-label"><textPath href="#arcSelf" startOffset="50%" text-anchor="middle">SELF DIRECTION</textPath></text>
    <text class="arc-label"><textPath href="#arcHuman" startOffset="50%" text-anchor="middle">HUMAN EXPERIENCE</textPath></text>
    <text class="arc-label"><textPath href="#arcEngage" startOffset="50%" text-anchor="middle">UNLEASH ENGAGEMENT</textPath></text>
    <g class="flow-arrows" fill="var(--paper)">
      <path d="M90,366 L77.3,374.5 L87.3,381.3 Z"/>
      <path d="M499.9,353.5 L495,339.1 L486,347.1 Z"/>
      <path d="M1072.9,724.8 L1065.5,738.2 L1058.1,728.8 Z"/>
    </g>
  </svg>
</div>
</body>
</html>
```